Financial Advisor Brochure to attract new clients

I am launching a new career as a Financial Advisor and a flier that shows what services I offer and why I decided to go back to work at this point in my life. I have a deep desire to help people meet their dreams and believe that a solid financial foundation provides the ability to live your life as you want to and not how you have to. I created a simple flier but know that so much more can be done to catch a persons eye.

Target Market(s)

Entrepeneurs and Woman in all stages of life.

Industry/Entity Type

Financial Advisor

Font styles to use
Sans Serif

Colors
00AB8E
00BBA5
67D7C9
C6EFE9
E9F9F6

Requirements
Must have
• my photo, contact information and Cobaltra Logo

```html
<!DOCTYPE html>
<html lang="en">
<head>
<meta charset="utf-8">
<title>Marla Hendrickx – Financial Advisor Flier</title>
<link href="https://fonts.googleapis.com/css2?family=Barlow+Condensed:wght@600;700&family=Montserrat:wght@400;500&display=swap" rel="stylesheet">
<style>
  :root{
    --green:#2db592;
    --teal:#35c1a7;
    --mint:#67d7c9;
    --pale:#c6efe9;
    --ice:#e9f9f6;
    --white:#ffffff;
    --ink:#2f3333;
    --backdrop:#c9c9c9;
  }
  *{margin:0;padding:0;box-sizing:border-box}
  html,body{width:1200px;height:2344px;overflow:hidden;background:var(--backdrop)}
  .flier{position:absolute;left:60px;top:408px;width:1080px;height:1528px;background:var(--white);overflow:hidden;box-shadow:0 6px 14px rgba(0,0,0,.35)}
  .flier-bg{position:absolute;inset:0}
  .abs{position:absolute}
  .display{font-family:"Barlow Condensed",Arial Narrow,sans-serif;font-weight:700;color:var(--white)}
  .body-font{font-family:"Montserrat",Arial,sans-serif}
  .advisor-name{left:44px;top:52px;font-size:66px;line-height:1;letter-spacing:.5px}
  .advisor-title{left:44px;top:128px;font-size:38px;font-weight:600;line-height:1}
  .section-label{left:44px;font-size:25px;font-weight:600;line-height:1}
  .profile-label{top:196px}
  .profile-text{left:44px;top:242px;width:440px;font-size:17.6px;font-weight:500;line-height:22px;color:var(--white)}
  .call-pill{left:38px;top:358px;width:305px;height:34px;background:var(--white);border-radius:7px;font-size:27px;color:var(--green);text-align:center;line-height:34px;font-weight:600}
  .phone-line{left:44px;top:404px;display:flex;align-items:center;gap:14px;font-size:42px;line-height:1}
  .email-label{top:477px}
  .website-label{top:556px}
  .contact-value{left:44px;font-size:17.5px;color:var(--white)}
  .email-value{top:510px}
  .website-value{top:589px}
  .story{left:47px;top:760px;width:404px;font-size:17.2px;line-height:22px;color:var(--ink);text-align:justify}
  .story p{margin-bottom:22px}
  .services-heading{left:544px;top:745px;font-size:36px;font-weight:600;line-height:1}
  .services{left:544px;top:800px;width:510px}
  .service{margin-bottom:14px}
  .service-tag{display:inline-block;background:var(--white);color:var(--green);border-radius:7px;padding:0 14px;height:34px;line-height:34px;font-family:"Barlow Condensed",Arial Narrow,sans-serif;font-weight:700;font-size:27px;margin-bottom:6px}
  .service ul{list-style:none;font-family:"Montserrat",Arial,sans-serif;font-size:17.5px;line-height:22px;color:var(--white)}
  .service li{position:relative;padding-left:20px;margin-bottom:5px}
  .service li::before{content:"";position:absolute;left:2px;top:8px;width:8px;height:8px;border-radius:50%;background:var(--white)}
</style>
</head>
<body>
<main class="flier">
  <svg class="flier-bg" width="1080" height="1528" viewBox="0 0 1080 1528">
    <defs>
      <linearGradient id="portraitFill" x1="0" y1="0" x2="0" y2="1">
        <stop offset="0" stop-color="#a7abab"/>
        <stop offset=".45" stop-color="#8e8f8c"/>
        <stop offset="1" stop-color="#1f9a82"/>
      </linearGradient>
    </defs>
    <rect class="teal-band" x="494" y="0" width="586" height="720" fill="var(--teal)"/>
    <path class="services-panel" d="M494 640 C700 600 900 600 1080 720 V1528 H494 Z" fill="var(--green)"/>
    <path class="accent-swoosh" d="M1010 590 C1050 620 1070 660 1080 700 V690 C1075 640 1050 600 1020 575 Z" fill="var(--pale)"/>
    <path class="header-panel" d="M0 0 H560 V588 C400 630 160 700 0 660 Z" fill="var(--teal)"/>
    <path class="header-accent" d="M0 660 C160 700 400 630 560 588 L560 600 C400 660 160 728 0 700 Z" fill="var(--pale)"/>
    <path class="portrait-frame" d="M500 0 H1040 V450 A270 270 0 0 1 500 450 Z" fill="url(#portraitFill)" stroke="var(--white)" stroke-width="6" role="img" aria-label="Portrait photo of the financial advisor, smiling, wearing a green blouse"/>
  </svg>

  <h1 class="abs display advisor-name">MARLA HENDRICKX</h1>
  <h2 class="abs display advisor-title">Financial Advisor</h2>
  <h3 class="abs display section-label profile-label">PROFILE</h3>
  <p class="abs body-font profile-text">Passionate about helping empower you with knowledge to make informed financial decisions throughout all of life’s stages and help you achieve your goals.</p>

  <div class="abs display call-pill">CALL FOR AN APPOINTMENT</div>
  <div class="abs display phone-line">
    <svg width="34" height="34" viewBox="0 0 24 24" aria-hidden="true"><path d="M6.6 2.5l2.6 3.9c.3.5.2 1.1-.2 1.5L7.6 9.2c1.3 2.9 3.6 5.2 6.5 6.6l1.3-1.4c.4-.4 1-.5 1.5-.2l3.9 2.5c.5.3.7 1 .4 1.5l-1.3 2.2c-.4.7-1.2 1.1-2 .9C10.6 19.5 4.5 13.4 2.6 6.1c-.2-.8.2-1.6.9-2L5.1 2.2c.5-.3 1.2-.2 1.5.3z" fill="#fff"/><path d="M14 2.5a8 8 0 0 1 7.5 7.5M14 6a4.5 4.5 0 0 1 4 4" fill="none" stroke="#fff" stroke-width="1.8" stroke-linecap="round"/></svg>
    <span>407-555-0182</span>
  </div>

  <h3 class="abs display section-label email-label">EMAIL:</h3>
  <p class="abs body-font contact-value email-value">marla.hendrickx@cobaltrawealthalliance.com</p>
  <h3 class="abs display section-label website-label">WEBSITE:</h3>
  <p class="abs body-font contact-value website-value">www.cobaltrawealthalliance.com</p>

  <article class="abs body-font story">
    <p>As a business owner, wife, and mother of two teenagers, I understand the struggles you face juggling your personal, business, and financial life.</p>
    <p>I grew up in a home where my parents had opposing money habits. My Dad was a big spender and mom was a saver. Through the years, I saw how my mom’s consistent savings grew while Dad’s style led to many financial ups and downs. This made a huge impression on me and sparked my continued interest in all things finance.</p>
    <p>Having an entrepreneurial personality and ability to explain concepts in a relatable manner has provided me with many opportunities. In 2018, After decades of running a sales agency, I sold my company to spend time with my kids and family but my interest in Finance never waned. Now that our kids are thriving teenagers, I started a new career as a licensed Financial Advisor with a heart to help you achieve your financial dreams.</p>
    <p>The financial world is changing rapidly, and it can be confusing on how to maneuver through these times. My goal is to pull out the emotions that cloud judgement and help you make better decisions with your long-range goals in mind</p>
  </article>

  <h2 class="abs display services-heading">Financial planning services offered:</h2>
  <section class="abs services">
    <div class="service"><span class="service-tag">Transition Planning</span>
      <ul><li>Divorce planning.</li><li>Strategy and guidance pre, during, and postdivorce</li></ul></div>
    <div class="service"><span class="service-tag">Retirement planning</span>
      <ul><li>Current portfolio analysis</li><li>Timeline asset and income planning</li><li>Tax and estate review and projections</li></ul></div>
    <div class="service"><span class="service-tag">Real estate acquisition or sale</span>
      <ul><li>Acquisition or dissolution of real estate. Individual or portfolio</li></ul></div>
    <div class="service"><span class="service-tag">Business sale or purchase:</span>
      <ul><li>Company valuations</li><li>Tax impact analysis</li><li>Strategy implementation for funds received from sale.</li></ul></div>
    <div class="service"><span class="service-tag">Estate planning</span>
      <ul><li>Strategies for creating future generational wealth.</li></ul></div>
    <div class="service"><span class="service-tag">New Investors:</span>
      <ul><li>Assistance in opening investment and retirement acc</li></ul></div>
  </section>
</main>
</body>
</html>
```